Poster of Core Values & Motto

Create our core values poster and motto. Attached are our core values and our Motto. This poster represents both of our companies Tidy Pulp & CuraBinix.

Target Market(s)

Our team / employees

Industry/Entity Type

Shredding and Medical Waste

Colors
59FF00
82FF00
B8FF75
E3FFCB
F4FFEA
EB3D1F
EC4F4E
F09395
F8D3D4
FCEDEE

Requirements
Must have
• Include both companies logos

```html
<!DOCTYPE html>
<html lang="en">
<head>
<meta charset="utf-8">
<title>Core Values Poster</title>
<link href="https://fonts.googleapis.com/css2?family=Poppins:wght@400;500;600;700&display=swap" rel="stylesheet">
<style>
  :root {
    --green: #27a349;
    --green-dark: #1f8a3b;
    --red: #d9262c;
    --red-dark: #b81c22;
    --ink: #111111;
    --paper: #f2f2f2;
    --paper-light: #fafafa;
    --stage: #e6e6e6;
    --white: #ffffff;
  }
  * { margin: 0; padding: 0; box-sizing: border-box; }
  html, body { width: 1200px; height: 1200px; overflow: hidden; }
  body {
    background: var(--stage);
    font-family: 'Poppins', sans-serif;
    color: var(--ink);
    position: relative;
  }
  .poster {
    position: absolute;
    left: 210px; top: 30px;
    width: 779px; height: 1140px;
    overflow: hidden;
    background: linear-gradient(135deg, var(--paper-light) 0%, var(--paper) 45%, #e9e9e9 60%, var(--paper-light) 100%);
    box-shadow: 0 4px 18px rgba(0,0,0,.12);
  }
  .brand {
    position: absolute;
    font-weight: 700;
    letter-spacing: 1px;
    display: flex; align-items: center; gap: 8px;
    top: 44px; font-size: 24px; line-height: 34px;
  }
  .brand-cura { left: 22px; color: var(--red); }
  .brand-tidy { right: 44px; color: var(--green); }
  .brand-dot { width: 26px; height: 26px; border-radius: 50%; background: var(--green); }
  .title-band {
    position: absolute; left: 0; top: 129px; width: 100%; height: 264px;
    background: var(--green);
    display: flex; flex-direction: column; align-items: center; justify-content: center;
  }
  .title-band h1 {
    color: var(--white); font-weight: 700; font-size: 84px; line-height: 80px;
    text-align: center; letter-spacing: 2px;
  }
  .value {
    position: absolute; display: flex; align-items: center; gap: 16px;
  }
  .value-icon {
    width: 82px; height: 82px; border-radius: 50%; flex: none;
    display: flex; align-items: center; justify-content: center;
  }
  .value-icon svg { width: 44px; height: 44px; }
  .icon-green { background: var(--green); }
  .icon-red { background: var(--red); }
  .icon-black { background: var(--ink); }
  .value-name { font-size: 20px; font-weight: 600; letter-spacing: 1px; line-height: 22px; }
  .value-desc { font-size: 13px; line-height: 15px; letter-spacing: .5px; margin-top: 2px; }
  .col-left { left: 35px; }
  .col-right { left: 399px; }
  .row-1 { top: 407px; }
  .row-2 { top: 522px; }
  .row-3 { top: 642px; }
  .motto { position: absolute; left: 43px; top: 766px; }
  .motto-words { font-size: 36px; font-weight: 500; line-height: 38px; }
  .motto-line { font-size: 31px; font-weight: 500; line-height: 41px; margin-top: 10px; letter-spacing: .5px; }
  .sharps-bin {
    position: absolute; left: 531px; top: 728px; width: 186px; height: 315px;
    background: linear-gradient(180deg, #e8eef2 0%, #e8eef2 22%, #e3363c 30%, #c81f26 100%);
    border-radius: 10px 10px 14px 14px;
  }
  .footer-arc { position: absolute; left: 0; bottom: 0; width: 779px; height: 118px; }
  .footer-links {
    position: absolute; left: 0; bottom: 6px; width: 100%; height: 30px;
    display: flex; justify-content: center; align-items: center;
    color: var(--white); font-size: 17px; letter-spacing: 1px;
  }
  .footer-links span { width: 240px; text-align: center; }
  .footer-divider { width: 1px !important; height: 30px; background: var(--white); margin: 0 38px; }
</style>
</head>
<body>
<main class="poster">
  <div class="brand brand-cura">CURABINIX</div>
  <div class="brand brand-tidy"><span class="brand-dot"></span>TIDY PULP</div>

  <header class="title-band"><h1>CORE<br>VALUSE</h1></header>

  <section class="value col-left row-1">
    <div class="value-icon icon-green">
      <svg viewBox="0 0 44 44" fill="#fff"><circle cx="22" cy="14" r="6"/><circle cx="11" cy="18" r="4.5"/><circle cx="33" cy="18" r="4.5"/><path d="M12 36c0-7 4-12 10-12s10 5 10 12z"/><path d="M3 34c0-5 3-9 8-9 2 0 3 .5 4 1-2 2-3 5-3 8z"/><path d="M41 34c0-5-3-9-8-9-2 0-3 .5-4 1 2 2 3 5 3 8z"/></svg>
    </div>
    <div><div class="value-name">SYERGY|TEAMWORK</div><div class="value-desc">Get it done attitude<br>with humble confidence</div></div>
  </section>
  <section class="value col-right row-1">
    <div class="value-icon icon-black">
      <svg viewBox="0 0 44 44" fill="none" stroke="#fff" stroke-width="2.5"><path d="M22 4l15 6v10c0 10-7 17-15 20C14 37 7 30 7 20V10z"/><rect x="16" y="21" width="12" height="9" fill="#fff"/><path d="M18 21v-3a4 4 0 0 1 8 0v3"/></svg>
    </div>
    <div><div class="value-name">SAFE AND SECURE</div><div class="value-desc">We are just as secure as an<br>armored truck with money.</div></div>
  </section>
  <section class="value col-left row-2">
    <div class="value-icon icon-red">
      <svg viewBox="0 0 44 44" fill="none" stroke="#fff" stroke-width="2.5"><circle cx="22" cy="17" r="11"/><path d="M17 17l4 4 7-7"/><path d="M15 26l-4 12 6-3 3 5 3-9M29 26l4 12-6-3-3 5"/></svg>
    </div>
    <div><div class="value-name">EXCELLENCE</div><div class="value-desc">Exceed ecpectations with a smile</div></div>
  </section>
  <section class="value col-right row-2">
    <div class="value-icon icon-green">
      <svg viewBox="0 0 44 44" fill="#fff"><path d="M22 39L6 23C1 18 2 9 9 7c5-1 9 2 13 6 4-4 8-7 13-6 7 2 8 11 3 16z"/></svg>
    </div>
    <div><div class="value-name">HONESTY | INTEGRITY</div><div class="value-desc">Do the right thing</div></div>
  </section>
  <section class="value col-left row-3">
    <div class="value-icon icon-black">
      <svg viewBox="0 0 44 44" fill="none" stroke="#fff" stroke-width="2.5"><circle cx="22" cy="22" r="13"/><path d="M22 4v5M22 35v5M4 22h5M35 22h5M9 9l4 4M31 31l4 4M9 35l4-4M31 13l4-4"/><path d="M22 22l5-6"/></svg>
    </div>
    <div><div class="value-name">EFFICIENT</div><div class="value-desc">On-time, sense of urgency,<br>always trying to improve</div></div>
  </section>
  <section class="value col-right row-3">
    <div class="value-icon icon-red">
      <svg viewBox="0 0 44 44" fill="none" stroke="#fff" stroke-width="2.5" stroke-linejoin="round"><path d="M3 18l8-6 6 3 5-3 6 1 12 5-6 8-9 7-4-3-4 1-8-6z"/><path d="M17 15l6 5M22 24l4 3M18 27l3 2"/></svg>
    </div>
    <div><div class="value-name">DEPENDABLE</div><div class="value-desc">Do what you say you will do.</div></div>
  </section>

  <section class="motto">
    <div class="motto-words">PURPOSE<br>CAUSE<br>PASSION</div>
    <div class="motto-line">Remind People What<br>Great Service Looks Like</div>
  </section>

  <div class="sharps-bin" role="img" aria-label="Red medical sharps container with open clear lid"></div>

  <svg class="footer-arc" viewBox="0 0 779 118" preserveAspectRatio="none">
    <path d="M0 118 Q389 -20 779 118 Z" fill="var(--ink)"/>
    <path d="M10 118 Q389 -6 769 118 Z" fill="var(--red)"/>
  </svg>
  <footer class="footer-links">
    <span>www.tidypulp.com</span><span class="footer-divider"></span><span>www.curabinix.com</span>
  </footer>
</main>
</body>
</html>
```